Communications Contractor Business Card Design

I would like a new business card for a new Communications company in Australia. Subcontracting and specialising in cabling, data, phone, antennas, pay tv ,modems, audio visual fibre optics etc. I am open to colour and design concepts but would like a modern clean look that stands out.

Industry/Entity Type

Tv

Contact Information for Business Card

quarzel communications pty ltd, Tomas Whitlock, PO BOX 527 Morrendale Flats QLD 4390 quarzel4me@mailbrook.net Australia. ph 0438271906. Director/Technician. services- Cabling,data,phone,antennas,audio visual,home theatre, fibre optics.

```html
<!DOCTYPE html>
<html lang="en">
<head>
<meta charset="utf-8">
<title>Quarzel Communications – Business Card</title>
<link rel="stylesheet" href="https://fonts.googleapis.com/css2?family=Arimo:wght@400;700&display=swap">
<style>
  :root {
    --page-bg: #e7e4df;
    --card-bg: #ffffff;
    --ink: #111111;
    --accent-red: #a3161a;
    --sky-top: #7f8fcf;
    --sky-mid: #c9c4e2;
    --sky-pink: #e7b3c6;
    --sky-low: #f3eef2;
    --shadow: rgba(0, 0, 0, 0.25);
  }
  * { box-sizing: border-box; margin: 0; padding: 0; }
  html, body {
    width: 1200px;
    height: 1200px;
    overflow: hidden;
    background: var(--page-bg);
    font-family: "Arimo", Arial, sans-serif;
    color: var(--ink);
  }
  .card {
    position: absolute;
    left: 139px;
    width: 919px;
    height: 565px;
    background: var(--card-bg);
    box-shadow: 0 4px 14px var(--shadow);
    overflow: hidden;
  }
  .card--front { top: 29px; }
  .card--back { top: 614px; }

  .sky-photo {
    position: absolute;
    right: 0;
    top: 0;
    width: 600px;
    height: 405px;
    background: linear-gradient(180deg, var(--sky-top) 0%, var(--sky-mid) 38%, var(--sky-pink) 62%, var(--sky-low) 85%, #ffffff 100%);
    -webkit-mask-image: linear-gradient(90deg, transparent 0%, #000 45%), linear-gradient(180deg, #000 75%, transparent 100%);
    -webkit-mask-composite: source-in;
    mask-image: linear-gradient(90deg, transparent 0%, #000 45%), linear-gradient(180deg, #000 75%, transparent 100%);
    mask-composite: intersect;
  }

  .brand-name {
    font-weight: 700;
    color: var(--ink);
    text-transform: uppercase;
    line-height: 1;
  }
  .brand-name__main { display: block; font-size: 72px; letter-spacing: -1px; }
  .brand-name__sub { display: block; font-size: 25px; letter-spacing: 1.5px; margin-top: 8px; }

  .card--front .brand-name {
    position: absolute;
    left: 43px;
    top: 58px;
  }

  .contact {
    position: absolute;
    left: 43px;
    top: 262px;
  }
  .contact__name { font-size: 31px; font-weight: 400; }
  .contact__role { font-size: 18px; font-weight: 700; margin-top: 4px; }
  .contact__line { font-size: 20px; margin-top: 14px; }
  .contact__line + .contact__line { margin-top: 10px; }

  .services {
    position: absolute;
    left: 43px;
    top: 464px;
  }
  .services__title { font-size: 25px; font-weight: 400; color: var(--accent-red); }
  .services__list { font-size: 22px; margin-top: 10px; white-space: nowrap; }

  .card--back .brand-name {
    position: absolute;
    left: 0;
    right: 0;
    top: 218px;
    text-align: center;
  }
</style>
</head>
<body>
  <section class="card card--front">
    <div class="sky-photo" role="img" aria-label="Photo of a communications tower with satellite dishes against a pastel sunset sky"></div>

    <div class="brand-name">
      <span class="brand-name__main">Quarzel</span>
      <span class="brand-name__sub">Communications Pty Ltd</span>
    </div>

    <div class="contact">
      <h1 class="contact__name">Tomas Whitlock</h1>
      <p class="contact__role">Director/Technician.</p>
      <p class="contact__line">PO BOX 527 Morrendale Flats QLD 4390 Australia.</p>
      <p class="contact__line">Phone : 0438271906.</p>
    </div>

    <div class="services">
      <h2 class="services__title">Services</h2>
      <p class="services__list">Cabling | data | phone | antennas | audio visual | home theatre | fibre optics.</p>
    </div>
  </section>

  <section class="card card--back">
    <div class="brand-name">
      <span class="brand-name__main">Quarzel</span>
      <span class="brand-name__sub">Communications Pty Ltd</span>
    </div>
  </section>
</body>
</html>
```